Brightpath Wellness needs a new services brochure

We need a new brochure that highlights the services that we offer at our clinic. We are a multidisciplinary health clinic that focuses on injury rehabilitation and pain management. We are looking for a brochure that will highlight our primary services to our clientele and inform potential clients of what we can offer. We pride ourselves on our quality of care and our advanced treatment techniques.
Target Market(s)
young families, athletes, people interested in their health.
Industry/Entity Type
Health And Wellness
Colors
Designer to choose colors to be used in the design.
Requirements
Must have
- We would love our new brochure to be a tri-fold that has 6 pages. We would like it to have brief information about our featured services:
- - Chiropractic
- - Massage Therapy
- - Manual Osteopathic Therapy
- - Acupuncture
- - Laser Therapy
- - Radial Shockwave Therapy
- We would also like this brochure to include a brief price list and direct billing info, About Us section & Contact information.
Nice to have
- If there is space to list that we also offer other services such as : Dynamic Tissue Method, Hot Stone Massage, Cupping Technique, Fascial Glide Technique, and Kinesiology Taping that would be great. We would like to use images similar to those that are on our website (we have hi-res of all images on the website) www.brightpathwellness.ca and colours that would fit with our logo.

```html
<!DOCTYPE html>
<html lang="en">
<head>
<meta charset="utf-8">
<title>Brightpath Wellness – Services Brochure</title>
<link href="https://fonts.googleapis.com/css2?family=Montserrat:wght@600;700;800&family=Open+Sans:wght@400;600;700&display=swap" rel="stylesheet">
<style>
  :root{
    --blue:#1d5a9c;
    --blue-dark:#143f70;
    --orange:#f28b1e;
    --paper:#ffffff;
    --ink:#3d4650;
    --muted:#66717d;
    --backdrop:#e4e5e7;
  }
  *{box-sizing:border-box;margin:0;padding:0}
  html,body{width:1200px;height:2400px;overflow:hidden}
  body{background:var(--backdrop);font-family:"Open Sans",Arial,sans-serif;color:var(--ink);position:relative}
  h2,h3,.tagline,.brand{font-family:"Montserrat",Arial,sans-serif}

  .spread{position:absolute;left:60px;width:1080px;height:835px;display:flex;background:var(--paper);box-shadow:0 6px 18px rgba(0,0,0,.12)}
  .spread--outside{top:325px}
  .spread--inside{top:1240px}
  .panel{width:360px;height:100%;position:relative;overflow:hidden}
  .panel + .panel{border-left:1px solid rgba(0,0,0,.05)}

  .photo{display:block}
  .section-bar{display:inline-block;padding:9px 24px 9px 30px;color:#fff;font-family:"Montserrat",Arial,sans-serif;font-weight:700;font-size:17px;text-transform:uppercase;letter-spacing:.5px;border-radius:0 22px 22px 0}
  .section-bar--blue{background:var(--blue)}
  .section-bar--orange{background:var(--orange)}
  .copy{font-size:13px;line-height:1.7;color:var(--muted)}
  .copy p + p{margin-top:12px}

  /* About */
  .about .photo{height:290px;background:linear-gradient(160deg,#b9a27e 0%,#8a7356 45%,#9fb3c4 100%)}
  .about .section-bar{margin-top:26px}
  .about .copy{padding:22px 30px 0}
  .about .footer-band{position:absolute;left:0;right:0;bottom:0;height:46px;background:var(--blue)}
  .about .footer-band::before{content:"";position:absolute;left:0;right:0;top:-6px;height:6px;background:var(--orange)}

  /* Contact */
  .contact{background:var(--blue);color:#fff;text-align:center}
  .contact .map{width:190px;height:190px;border-radius:50%;margin:48px auto 0;border:6px solid #fff;background:linear-gradient(135deg,#eef0ea,#cfd8cf 60%,#e2e6df)}
  .contact .section-bar{margin:34px 0 0;border-radius:22px;padding:9px 34px}
  .contact .lines{margin-top:20px;font-size:13.5px;line-height:2}
  .contact .lines svg{vertical-align:-2px;margin-right:6px}
  .hours{margin:26px auto 0;width:250px}
  .hours h3{font-size:16px;font-weight:700;color:var(--orange);text-transform:uppercase;margin-bottom:10px}
  .hours table{width:100%;border-collapse:collapse;font-size:13px}
  .hours td{padding:5px 0;border-bottom:1px solid rgba(255,255,255,.18);text-align:left}
  .hours td:last-child{text-align:right}
  .contact .web{position:absolute;left:0;right:0;bottom:0;background:var(--orange);padding:14px 0;font-weight:700;font-size:14px;letter-spacing:.3px}

  /* Cover */
  .cover .swoosh{position:absolute;left:0;width:360px}
  .cover .swoosh--top{top:0}
  .cover .swoosh--bottom{bottom:0}
  .brand{position:absolute;top:100px;right:30px;display:flex;align-items:center;gap:10px;color:var(--blue);font-weight:700;font-size:21px;white-space:nowrap}
  .brand .dot{width:26px;height:26px;border-radius:50%;background:var(--orange);flex:none}
  .cover .photo{position:absolute;top:150px;left:0;width:360px;height:360px;background:linear-gradient(150deg,#e9d9c2 0%,#c8a98a 40%,#88a7c9 75%,#a6c58f 100%);clip-path:ellipse(120% 100% at 80% 0%)}
  .tagline{position:absolute;top:540px;left:0;right:0;text-align:center;font-weight:800;line-height:1.15}
  .tagline .l1{display:block;color:var(--blue);font-size:25px}
  .tagline .l2{display:block;color:var(--orange);font-size:30px}
  .phone-pill{position:absolute;top:650px;left:60px;right:60px;background:var(--blue);color:#fff;border-radius:24px;text-align:center;padding:11px 0;font-weight:700;font-size:16px}
  .phone-pill svg{vertical-align:-3px;margin-right:8px}

  /* Inside: services */
  .services-a .photo{position:relative;height:250px;background:linear-gradient(120deg,#7fa35e 0%,#b4c98c 45%,#d9cba5 100%)}
  .services-a .photo-caption{position:absolute;right:26px;top:70px;text-align:right;color:#fff;font-family:"Montserrat",Arial,sans-serif;font-weight:800;font-size:28px;line-height:1;text-shadow:0 1px 3px rgba(0,0,0,.25)}
  .services-a .photo-caption em{display:block;font-style:normal;font-weight:600;font-size:22px;color:var(--orange)}
  .services-a .section-bar{margin-top:22px}
  .service{padding:0 30px;margin-top:20px}
  .service h3{font-size:15px;font-weight:700;color:var(--blue);text-transform:uppercase;margin-bottom:5px}
  .service .copy{font-size:12.5px;line-height:1.65}
  .services-b{padding-top:40px}
  .services-b .service{margin-top:26px}
  .services-b .service:first-child{margin-top:0}
  .other-list{list-style:none;font-size:13px;color:var(--muted);line-height:2}
  .other-list li::before{content:"";display:inline-block;width:7px;height:7px;border-radius:50%;background:var(--orange);margin-right:10px;vertical-align:2px}
  .billing{margin:30px 30px 0;border-top:2px solid var(--orange);padding-top:18px}
  .billing .section-bar{margin-left:-30px}
  .billing .copy{margin-top:14px;font-size:12.5px}

  /* Prices */
  .prices{background:var(--blue);color:#fff}
  .prices .section-bar{margin-top:48px}
  .price-table{margin:26px 30px 0;width:300px;border-collapse:collapse;font-size:13px}
  .price-table th{text-align:left;color:var(--orange);font-family:"Montserrat",Arial,sans-serif;font-size:14px;text-transform:uppercase;padding:18px 0 6px}
  .price-table td{padding:8px 0;border-bottom:1px dashed rgba(255,255,255,.25)}
  .price-table td:last-child{text-align:right;font-weight:700}
  .prices .note{margin:30px 30px 0;font-size:12px;line-height:1.65;color:rgba(255,255,255,.82)}
</style>
</head>
<body>

<section class="spread spread--outside">
  <article class="panel about">
    <div class="photo" role="img" aria-label="Photo of the clinic building exterior"></div>
    <h2 class="section-bar section-bar--blue">About Us</h2>
    <div class="copy">
      <p>Brightpath Wellness is a multidisciplinary clinic focused on injury rehabilitation and pain management. Our team works together to build a care plan that fits your goals and your lifestyle.</p>
      <p>We pride ourselves on quality of care and advanced treatment techniques, helping young families, athletes and anyone who values their health get back to doing what they love.</p>
      <p>From your first assessment to your final visit, we listen, explain every step and track your progress so you always know where you stand.</p>
      <p>Book an assessment today and let us help you move better and feel better.</p>
    </div>
    <div class="footer-band"></div>
  </article>

  <article class="panel contact">
    <div class="map" role="img" aria-label="Map showing the clinic location"></div>
    <h2 class="section-bar section-bar--orange">Contact Us</h2>
    <div class="lines">
      <div><svg width="12" height="14" viewBox="0 0 12 14"><path d="M6 0a5 5 0 0 0-5 5c0 4 5 9 5 9s5-5 5-9a5 5 0 0 0-5-5zm0 7a2 2 0 1 1 0-4 2 2 0 0 1 0 4z" fill="#fff"/></svg>210 Maple Crest Drive, Calgary AB</div>
      <div><svg width="13" height="13" viewBox="0 0 24 24"><path d="M6.6 10.8a15 15 0 0 0 6.6 6.6l2.2-2.2c.3-.3.7-.4 1-.2 1.1.4 2.3.6 3.6.6.6 0 1 .4 1 1V20c0 .6-.4 1-1 1A17 17 0 0 1 3 4c0-.6.4-1 1-1h3.5c.6 0 1 .4 1 1 0 1.3.2 2.5.6 3.6.1.3 0 .7-.2 1z" fill="#fff"/></svg>(403) 555-0142</div>
      <div>hello@brightpathwellness.ca</div>
    </div>
    <div class="hours">
      <h3>Hours</h3>
      <table>
        <tr><td>Monday – Thursday</td><td>8am – 8pm</td></tr>
        <tr><td>Friday</td><td>8am – 6pm</td></tr>
        <tr><td>Saturday</td><td>9am – 3pm</td></tr>
        <tr><td>Sunday</td><td>Closed</td></tr>
      </table>
    </div>
    <div class="web">www.brightpathwellness.ca</div>
  </article>

  <article class="panel cover">
    <svg class="swoosh swoosh--top" height="150" viewBox="0 0 360 150" preserveAspectRatio="none">
      <path d="M0 0h360v22C250 10 120 30 0 80z" fill="var(--blue)"/>
      <path d="M0 80C120 30 250 10 360 22v8C250 20 120 42 0 92z" fill="var(--orange)"/>
    </svg>
    <div class="brand"><span class="dot"></span>Brightpath Wellness</div>
    <div class="photo" role="img" aria-label="Photo of a smiling family together outdoors"></div>
    <p class="tagline"><span class="l1">HELPING YOU LIVE LIFE</span><span class="l2">PAIN FREE</span></p>
    <div class="phone-pill"><svg width="16" height="16" viewBox="0 0 24 24"><path d="M6.6 10.8a15 15 0 0 0 6.6 6.6l2.2-2.2c.3-.3.7-.4 1-.2 1.1.4 2.3.6 3.6.6.6 0 1 .4 1 1V20c0 .6-.4 1-1 1A17 17 0 0 1 3 4c0-.6.4-1 1-1h3.5c.6 0 1 .4 1 1 0 1.3.2 2.5.6 3.6.1.3 0 .7-.2 1z" fill="#fff"/></svg>(403) 555-0142</div>
    <svg class="swoosh swoosh--bottom" height="90" viewBox="0 0 360 90" preserveAspectRatio="none">
      <path d="M0 60C130 40 250 50 360 20v8C250 58 130 48 0 68z" fill="var(--orange)"/>
      <path d="M0 68C130 48 250 58 360 28v62H0z" fill="var(--blue)"/>
    </svg>
  </article>
</section>

<section class="spread spread--inside">
  <article class="panel services-a">
    <div class="photo" role="img" aria-label="Photo of a woman stretching outdoors on a sunny day">
      <p class="photo-caption">LIVE LIFE<em>pain free</em></p>
    </div>
    <h2 class="section-bar section-bar--orange">Our Services</h2>
    <div class="service">
      <h3>Chiropractic</h3>
      <p class="copy">Gentle adjustments restore joint motion, ease back and neck pain and support healthy posture for every age.</p>
    </div>
    <div class="service">
      <h3>Massage Therapy</h3>
      <p class="copy">Registered therapists release muscle tension, improve circulation and speed recovery from injury or training.</p>
    </div>
    <div class="service">
      <h3>Manual Osteopathic Therapy</h3>
      <p class="copy">Hands-on techniques treat the whole body, improving mobility and balance between muscles, joints and organs.</p>
    </div>
    <div class="service">
      <h3>Acupuncture</h3>
      <p class="copy">Fine needles stimulate natural healing, reduce pain and help manage stress, headaches and chronic conditions.</p>
    </div>
  </article>

  <article class="panel services-b">
    <div class="service">
      <h3>Laser Therapy</h3>
      <p class="copy">Low-level laser light reduces inflammation and accelerates tissue repair without any downtime.</p>
    </div>
    <div class="service">
      <h3>Radial Shockwave Therapy</h3>
      <p class="copy">Acoustic pulses break down scar tissue and relieve stubborn tendon pain such as plantar fasciitis.</p>
    </div>
    <div class="service">
      <h3>Other Services</h3>
      <ul class="other-list">
        <li>Dynamic Tissue Method</li>
        <li>Hot Stone Massage</li>
        <li>Cupping Technique</li>
        <li>Fascial Glide Technique</li>
        <li>Kinesiology Taping</li>
      </ul>
    </div>
    <div class="billing">
      <h3 class="section-bar section-bar--blue">Direct Billing</h3>
      <p class="copy">We bill most major insurance providers directly, so you pay only your portion at the time of your visit. Ask our front desk for details about your plan and coverage.</p>
    </div>
  </article>

  <article class="panel prices">
    <h2 class="section-bar section-bar--orange">Our Prices</h2>
    <table class="price-table">
      <tr><th colspan="2">Chiropractic</th></tr>
      <tr><td>Initial Assessment</td><td>$85</td></tr>
      <tr><td>Follow-up Visit</td><td>$55</td></tr>
      <tr><th colspan="2">Massage Therapy</th></tr>
      <tr><td>30 Minutes</td><td>$60</td></tr>
      <tr><td>60 Minutes</td><td>$95</td></tr>
      <tr><th colspan="2">Osteopathic Therapy</th></tr>
      <tr><td>60 Minutes</td><td>$110</td></tr>
      <tr><th colspan="2">Acupuncture</th></tr>
      <tr><td>Treatment</td><td>$75</td></tr>
      <tr><th colspan="2">Laser &amp; Shockwave</th></tr>
      <tr><td>Per Session</td><td>$65</td></tr>
    </table>
    <p class="note">Prices include applicable taxes. Package rates are available for ongoing care plans.</p>
  </article>
</section>

</body>
</html>
```